Brightmoor Business Solutions

I need a business card design with logo for my business and management consultancy business. I am based in Singapore and I provide (i) accounting / bookkeeping services; (ii) management and business consultancy solutions; (iii) tax advisory and consultancy; and (iv) risk management and corporate governance. I want the design to be bold and outstanding yet doesn't give the impression that I take unnecessary risks.

Reason: To the designers who have gotten messages from me, I'm still waiting for some changes to be made.

Target Market(s)

Small to large enterprises which are willing to pay value for money and not necessarily the cheapest

Industry/Entity Type

Accounting

Contact Information for Business Card

Name, email address and mobile no.

Requirements
Must have
• If possible, could you incorporate the Sigma symbol as the E for Brightmoor or the Equals sign to show that the business relates to finance / financials and that I provide solutions which may it easy for my clients.
Should not have
• Black / dark backgrounds

```html
<!DOCTYPE html>
<html lang="en">
<head>
<meta charset="utf-8">
<title>Brightmoor Business Card</title>
<link rel="stylesheet" href="https://fonts.googleapis.com/css2?family=Ubuntu:wght@500;700&family=Arimo:wght@700&display=swap">
<style>
  :root {
    --backdrop: #ababab;
    --card: #ffffff;
    --blue-light: #72aad6;
    --blue-deep: #2b6189;
    --blue-logo: #4f8dbf;
    --ink: #333333;
    --on-blue: #ffffff;
  }
  * { margin: 0; padding: 0; box-sizing: border-box; }
  html, body { width: 1200px; height: 960px; overflow: hidden; }
  body { background: var(--backdrop); position: relative; font-family: "Arimo", Arial, sans-serif; }

  .card {
    position: absolute; left: 192px; top: 221px;
    width: 820px; height: 474px;
    background: var(--card); overflow: hidden;
  }
  .card-shapes { position: absolute; inset: 0; width: 100%; height: 100%; }

  .brand-name {
    position: absolute; left: 150px; top: 44px;
    font-family: "Ubuntu", Arial, sans-serif; font-weight: 700;
    font-size: 44px; color: var(--blue-logo); letter-spacing: 0.5px;
  }

  .person { position: absolute; right: 90px; top: 252px; text-align: right; }
  .person-name {
    font-family: "Ubuntu", Arial, sans-serif; font-weight: 700;
    font-size: 31px; color: var(--blue-deep); line-height: 1.1;
  }
  .person-role { font-size: 17px; color: var(--ink); margin-top: 4px; }

  .contact {
    position: absolute; display: flex; align-items: center; gap: 10px;
    color: var(--on-blue); font-size: 18px;
  }
  .contact svg { width: 16px; height: 16px; fill: var(--on-blue); }
  .contact-address { left: 150px; top: 388px; }
  .contact-phone { left: 150px; top: 418px; }
  .contact-web { left: 350px; top: 418px; }

  .brand-standalone {
    position: absolute; left: 760px; top: 820px;
    font-family: "Ubuntu", Arial, sans-serif; font-weight: 700;
    font-size: 64px; color: var(--blue-logo);
  }
</style>
</head>
<body>
  <section class="card" aria-label="Business card">
    <svg class="card-shapes" viewBox="0 0 683 395" preserveAspectRatio="none" aria-hidden="true">
      <defs>
        <linearGradient id="band-fade" x1="0" y1="0" x2="0" y2="1">
          <stop offset="0" stop-color="var(--blue-light)"/>
          <stop offset="0.8" stop-color="var(--blue-deep)"/>
          <stop offset="1" stop-color="var(--blue-deep)"/>
        </linearGradient>
      </defs>
      <polygon class="chevron-band" fill="url(#band-fade)"
        points="0,0 85,0 228,126 112,311 683,311 683,395 0,395 0,326 135,131 0,12"/>
    </svg>

    <div class="brand-name">Brightmoor</div>

    <div class="person">
      <div class="person-name">Daniel Reyes</div>
      <div class="person-role">consultant</div>
    </div>

    <div class="contact contact-address">
      <svg viewBox="0 0 16 16"><path d="M8 1 1 8h2v7h4v-4h2v4h4V8h2z"/></svg>
      <span>Lindell Rd</span>
    </div>
    <div class="contact contact-phone">
      <svg viewBox="0 0 16 16"><path d="M4 1 6.5 4 5 6c1 2 3 4 5 5l2-1.5 3 2.5-1.5 3C7 15 1 9 1 2.5z"/></svg>
      <span>987.654.321</span>
    </div>
    <div class="contact contact-web">
      <svg viewBox="0 0 16 16"><path d="M8 1a7 7 0 1 0 0 14A7 7 0 0 0 8 1zm0 2a5 5 0 0 1 4.5 2.8L9 7 7 5V3.1zM3.2 6.5 6 9l-1 3.7A5 5 0 0 1 3.2 6.5z"/></svg>
      <span>www.brightmoor.com</span>
    </div>
  </section>

  <div class="brand-standalone">Brightmoor</div>
</body>
</html>
```